Online Marketing Agency Website

We are an online marketing agency that specializes in search marketing (SEM) for businesses of all sizes. Our core services include local search marketing, seo, paid search, paid social, graphic design, video production/editing and website design. We have an existing website that we launched a number of years ago but it's very outdated and we're currently too busy to design a new version.

Target Market(s)

Any business that needs online marketing services with an emphasis on search marketing.

Industry/Entity Type

Ad Agency

Number of Pages Required

4 page

Font styles to use
Sans Serif

Requirements
Must have
• Home page, interior page, blog page, contact us page.
Look and feel should be modern and clean and easy to navigate.
Sections for call outs for specific services: Business Marketing Strategy, Content Creation and Marketing, Graphic & Publication Design, Pay Per Click (PPC) Management, Search Engine Optimization, Social Media Management, Video Production & Editing, Website Hosting & Management, Website Design & Development
Use color from logo that was uploaded.

```html
<!DOCTYPE html>
<html lang="en">
<head>
<meta charset="utf-8">
<title>Lumen Reach — Online Marketing Agency</title>
<link href="https://fonts.googleapis.com/css2?family=Heebo:wght@300;400;500;700&display=swap" rel="stylesheet">
<style>
:root{
  --accent:#ef4a25;
  --ink:#222326;
  --muted:#6c6f75;
  --dark:#2d2e33;
  --light:#f6f6f7;
  --white:#ffffff;
}
*{box-sizing:border-box;margin:0;padding:0}
html,body{width:1200px;height:3686px;overflow:hidden}
body{font-family:"Heebo",Arial,sans-serif;color:var(--ink);background:var(--white);position:relative}
.abs{position:absolute}
.center{left:0;width:1200px;text-align:center}
.tag{display:inline-block;background:var(--accent);color:#fff;font-size:11px;font-weight:700;letter-spacing:1px;padding:5px 10px;border-radius:3px}
/* nav */
.nav{top:0;left:0;width:1200px;height:112px;background:#fff}
.nav a{position:absolute;font-size:11px;font-weight:700;color:var(--ink);text-decoration:none;letter-spacing:.3px}
.nav .active{border-bottom:3px solid var(--accent);padding:0 16px 12px}
.brand{position:absolute;left:520px;top:14px;width:160px;text-align:center}
.brand .mark{width:30px;height:30px;border-radius:50%;background:var(--accent);margin:0 auto 6px}
.brand b{display:block;font-size:14px;font-weight:700;color:var(--ink)}
.brand small{display:block;font-size:8.5px;color:var(--muted)}
.btn-outline{position:absolute;border:2px solid var(--accent);color:var(--ink);font-size:11px;font-weight:700;text-align:center}
/* hero */
.hero{top:112px;left:0;width:1200px;height:588px;background:linear-gradient(90deg,#2b2c31 0%,#3a3b40 45%,#6a6665 70%,#8a7f78 100%)}
.hero h1{font-size:48px;font-weight:400;color:#fff;line-height:56px}
.hero p{font-size:14px;color:#d8d8d8}
.dot{position:absolute;border-radius:50%;background:rgba(255,255,255,.08)}
.dot i{position:absolute;left:50%;top:50%;border-radius:50%;background:var(--accent);transform:translate(-50%,-50%)}
/* about */
.wave{top:700px;left:0;width:1200px;height:90px}
.about h2{font-size:31px;font-weight:400}
.about p{font-size:12px;color:var(--muted);line-height:19px}
.video{left:283px;top:1012px;width:633px;height:422px;border-radius:8px;background:linear-gradient(135deg,#4a3a36 0%,#6d5a52 40%,#3e5470 75%,#2a2c33 100%)}
.play{position:absolute;left:281px;top:176px;width:70px;height:70px;border-radius:50%;border:3px solid rgba(255,255,255,.8)}
.play:after{content:"";position:absolute;left:27px;top:20px;border-left:20px solid rgba(255,255,255,.85);border-top:12px solid transparent;border-bottom:12px solid transparent}
.clients{top:1565px;left:300px;width:600px;display:flex;justify-content:space-between;align-items:center}
.clients span{font-size:20px;font-weight:500;color:#c4c5c8}
/* services */
.services{top:1688px;left:0;width:1200px;height:700px;background:linear-gradient(120deg,#2b2c30 0%,#34353a 55%,#57514f 80%,#6b6360 100%)}
.services h2{font-size:40px;font-weight:400;color:#fff}
.svc{position:absolute;width:240px;color:#fff}
.svc .ic{position:absolute;left:0;top:0;width:36px;height:36px;border-radius:50%;background:#fff}
.svc .ic:after{content:"";position:absolute;left:14px;top:14px;width:8px;height:8px;border-radius:2px;background:var(--dark)}
.svc h3{margin-left:47px;font-size:13px;font-weight:500;letter-spacing:-.3px}
.svc p{margin-left:47px;font-size:10px;line-height:16px;color:#c9c9cc;margin-top:3px}
/* testimonials */
.testi h2{font-size:29px;font-weight:400}
.card{position:absolute;top:2620px;width:413px;height:249px;background:var(--light);text-align:center;padding:46px 40px 0}
.card p{font-size:12px;line-height:20px;color:var(--muted)}
.who{display:flex;justify-content:center;align-items:center;margin-top:16px;text-align:left}
.who .av{width:46px;height:46px;border-radius:50%;background:linear-gradient(#c9a38a,#7a5a4c);margin-right:12px}
.who b{display:block;font-size:12px;font-weight:700}
.who small{font-size:10px;font-weight:500;letter-spacing:1px;color:var(--accent)}
/* band */
.band{top:3046px;left:0;width:1200px;height:340px;background:linear-gradient(120deg,#2a2b30 0%,#3c3d44 50%,#4e4a4a 100%)}
.band h2{font-size:29px;font-weight:400;color:#fff;line-height:36px}
.social{display:flex;gap:18px;justify-content:center}
.social span{width:55px;height:55px;border-radius:50%;background:rgba(255,255,255,.08);position:relative}
.social span:after{content:"";position:absolute;left:21px;top:21px;width:13px;height:13px;border-radius:50%;background:var(--accent)}
/* footer */
.footer{top:3386px;left:0;width:1200px;height:300px;background:var(--light)}
.flinks a{display:block;font-size:10px;color:var(--ink);text-decoration:none;margin-bottom:24px}
.footer h2{font-size:31px;font-weight:700}
.input{position:absolute;left:507px;top:3578px;width:262px;height:38px;border:1px solid #ccc;background:#fff;font-size:11px;color:#999;padding:11px 12px}
.sub{position:absolute;left:776px;top:3578px;width:172px;height:38px;background:var(--accent);color:#fff;font-size:14px;font-weight:700;text-align:center;line-height:38px}
</style>
</head>
<body>

<header class="abs nav">
  <a class="active" href="#" style="left:284px;top:49px">HOME</a>
  <a href="#" style="left:364px;top:49px">SERVICES ▾</a>
  <a href="#" style="left:458px;top:49px">BLOG</a>
  <div class="brand"><div class="mark"></div><b>LUMEN REACH</b><small>Online Marketing. Elevated</small></div>
  <a href="#" style="left:697px;top:49px">CALL 555-010-274</a>
  <div class="btn-outline" style="left:801px;top:37px;width:108px;height:36px;line-height:32px">CONTACT</div>
</header>

<section class="abs hero">
  <div class="abs" role="img" aria-label="Photo of two colleagues discussing work at a tablet" style="left:560px;top:0;width:640px;height:588px;background:linear-gradient(90deg,rgba(43,44,49,0),rgba(140,125,115,.35))"></div>
  <div class="dot" style="left:71px;top:168px;width:60px;height:60px"><i style="width:14px;height:14px"></i></div>
  <div class="dot" style="left:253px;top:202px;width:36px;height:36px"><i style="width:8px;height:8px"></i></div>
  <div class="dot" style="left:146px;top:371px;width:82px;height:82px"><i style="width:18px;height:18px"></i></div>
  <div class="dot" style="left:278px;top:373px;width:52px;height:52px"><i style="width:12px;height:12px"></i></div>
  <div class="dot" style="left:1070px;top:160px;width:74px;height:74px"><i style="width:18px;height:18px"></i></div>
  <div class="dot" style="left:886px;top:262px;width:70px;height:70px;background:none"><i style="width:30px;height:30px"></i></div>
  <div class="dot" style="left:1089px;top:420px;width:36px;height:36px"><i style="width:8px;height:8px"></i></div>
  <div class="abs center" style="top:112px"><span class="tag">MARA ELLISON</span></div>
  <h1 class="abs center" style="top:158px">Online Marketing<br>Agency</h1>
  <p class="abs center" style="top:270px">Lumen Reach is a full-service online marketing agency.</p>
  <div class="btn-outline" style="left:504px;top:325px;width:192px;height:46px;line-height:42px;color:#fff">Social Media Services</div>
</section>

<svg class="abs wave" viewBox="0 0 1200 90" preserveAspectRatio="none"><path d="M0 0H1200V40C1000 80 850 10 600 50C380 85 200 20 0 55Z" fill="#f4f4f5"/></svg>

<section class="about">
  <div class="abs center" style="top:784px"><span class="tag">ABOUT ME</span></div>
  <h2 class="abs center" style="top:832px">Online marketing and social media strategy.</h2>
  <p class="abs center" style="top:888px">We can handle any element of your online marketing so you can get back to doing what you do best — growing your<br>business. All of our services are offered on an 'a la carte' basis</p>
  <div class="abs video" role="img" aria-label="Video still of a team meeting around a laptop"><div class="play"></div></div>
  <p class="abs center" style="top:1512px;font-size:11px;font-weight:700;letter-spacing:1px;color:var(--ink)">TRUSTED BY CLIENTS LIKE</p>
  <div class="abs clients"><span>Orvel</span><span>Corvane</span><span>Wavio</span><span>Rook</span><span>Tessly</span></div>
</section>

<section class="abs services">
  <div class="abs" role="img" aria-label="Photo of hands over a desk with laptop and charts" style="left:600px;top:0;width:600px;height:700px;background:linear-gradient(90deg,rgba(0,0,0,0),rgba(120,110,105,.3))"></div>
  <h2 class="abs center" style="top:76px">My Services</h2>
  <div class="svc" style="left:269px;top:188px"><span class="ic"></span><h3>Business Marketing Strategy</h3><p>Let us strategize the big picture for you. With decades of experience, we have seen what works</p></div>
  <div class="svc" style="left:528px;top:188px"><span class="ic"></span><h3>Content Creation and Marketing</h3><p>You've heard it before. "Content is king." Search loves it and potential customers expect it.</p></div>
  <div class="svc" style="left:787px;top:188px"><span class="ic"></span><h3>Graphic &amp; Publication Design</h3><p>Our designers have decades of experience in everything from tradeshow graphics to magazine layouts</p></div>
  <div class="svc" style="left:269px;top:311px"><span class="ic"></span><h3>Pay Per Click (PPC) Management</h3><p>PPC advertising delivers some of the best ROI online…but it can be overwhelming. Let us research your best keywords,</p></div>
  <div class="svc" style="left:528px;top:311px"><span class="ic"></span><h3>Search Engine Optimization</h3><p>The SEO playing field is shifting constantly. From week to week, the rules change and your rankings can drop.</p></div>
  <div class="svc" style="left:787px;top:311px"><span class="ic"></span><h3>Social Media Management</h3><p>Scratching your head over how to make social media work for you? Our team has proven strategies that will help</p></div>
  <div class="svc" style="left:269px;top:434px"><span class="ic"></span><h3>Video Production &amp; Editing</h3><p>Video content is absolutely key in today's SEO landscape. From scripting to publishing,</p></div>
  <div class="svc" style="left:528px;top:434px"><span class="ic"></span><h3>Website Hosting &amp; Management</h3><p>We will find you the most affordable, most-appropriate-for-your-business hosting solutions.</p></div>
  <div class="svc" style="left:787px;top:434px"><span class="ic"></span><h3>Website Design &amp; Development</h3><p>Nothing will kill your business faster than a dated, unattractive or confusing website. Let us show you the most modern,</p></div>
  <div class="btn-outline" style="left:517px;top:575px;width:166px;height:44px;line-height:40px;color:#fff">View All Services</div>
</section>

<section class="testi">
  <div class="abs center" style="top:2465px"><span class="tag">TESTIMONIALS</span></div>
  <h2 class="abs center" style="top:2515px">What Our Client Says</h2>
  <div class="card" style="left:174px">
    <p>"Sed ut perspiciatis unde omnis iste natus error sit voluptatem accusantium doloremque laudantium, totam rem aperiam. At vero eos et bitse. At vero eos et accusamus et iusto odio dignissimos ducimus qui blanditiis prtium voluptatum."</p>
    <div class="who"><span class="av" role="img" aria-label="Client portrait"></span><div><b>Nora Vidal</b><small>INFLUENCER</small></div></div>
  </div>
  <div class="card" style="left:612px">
    <p>"Cupiditate non provident, similique sunt in culpa qui officia deserunt mollitia animi, id est laborum et dolorum fuga. totam rem aperiam. At vero eos et bitse. At vero eos et accusamus et iusto Cupiditate non provident, similique sunt in culpa qui officiel."</p>
    <div class="who"><span class="av" role="img" aria-label="Client portrait"></span><div><b>Tobin Harte</b><small>INFLUENCER</small></div></div>
  </div>
  <p class="abs center" style="top:2908px;font-size:14px;color:var(--muted)">Want to see all our client reviews &amp; testimonials?</p>
  <p class="abs center" style="top:2936px;font-size:15px;font-weight:500">See More Testimonials</p>
</section>

<section class="abs band" role="img" aria-label="Photo of people working with laptops and tablets">
  <h2 class="abs center" style="top:68px">Enhancing communication with<br>customers</h2>
  <div class="abs social" style="left:0;width:1200px;top:160px"><span></span><span></span><span></span><span></span><span></span></div>
  <p class="abs center" style="top:260px;font-size:12px;color:#e5e5e5;line-height:19px">Engaging our followers on social media platforms to let them know<br>about our work</p>
</section>

<footer class="abs footer">
  <div class="abs" style="left:150px;top:82px;width:142px;text-align:center">
    <div style="width:30px;height:30px;border-radius:50%;background:var(--accent);margin:0 auto 8px"></div>
    <b style="display:block;font-size:14px">LUMEN REACH</b>
    <small style="font-size:8.5px;color:var(--muted)">Online Marketing. Elevated</small>
  </div>
  <nav class="abs flinks" style="left:343px;top:84px"><a href="#">Faq</a><a href="#">Term And Condition</a><a href="#">Privacy and Policy</a><a href="#">Contact</a></nav>
  <h2 class="abs" style="left:507px;top:76px">Subscribe To Us</h2>
  <p class="abs" style="left:507px;top:132px;width:510px;font-size:10px;line-height:16px;color:var(--ink)">Lorem ipsum dolor sit amet, consectetur adipiscing elit. Ut elit tellus, luctus nec ullamcorper mattis, pulvinar dapibus leo.</p>
</footer>
<div class="input">Email</div>
<div class="sub">SUBSCRIBE</div>

</body>
</html>
```